Certificates with Watermark Images

We are looking for a design of One page Certificates with Watermark (background) images where text will be printed over it .
Graphics design is required to reflect the flowing categories:
IPTV (Internet Protocol TV)
VoD (Video on Demand)
Satellite Receiver
Graphics design images for all three categories must be provided to maintain the same them .
Thank you and good luck.
Industry/Entity Type
Internet
Requirements
Must have
- Graphics design images for all three categories must be provided to maintain the same them

```html
<!DOCTYPE html>
<html lang="en">
<head>
<meta charset="utf-8">
<title>Certificate of Achievement</title>
<link rel="stylesheet" href="https://fonts.googleapis.com/css2?family=UnifrakturMaguntia&family=Cormorant+Garamond:wght@500;600&display=swap">
<style>
  :root {
    --page: #f2f0e4;
    --panel: #f8f5e6;
    --panel-edge: #e9cf9f;
    --band-peach: #f1c99a;
    --band-cream: #f6e3c6;
    --band-lilac: #c9aecb;
    --rosette-core: #e3b28d;
    --rosette-light: #fbe9d5;
    --gold: #b8983a;
    --gold-line: #d6bf78;
    --title-grey: #5e5e5e;
    --icon-light: #e4e4e4;
    --icon-mid: #bdbdbd;
  }
  * { margin: 0; padding: 0; box-sizing: border-box; }
  html, body { width: 1200px; height: 849px; overflow: hidden; background: var(--page); }
  .certificate { position: relative; width: 1200px; height: 849px; background: var(--page); overflow: hidden; }

  .border-band {
    position: absolute; left: 20px; top: 22px; width: 1160px; height: 806px;
    border-radius: 60px;
    background:
      linear-gradient(var(--band-cream), var(--band-cream)) padding-box,
      linear-gradient(135deg, var(--band-peach), var(--band-lilac) 30%, var(--band-peach) 55%, var(--band-lilac) 80%, var(--band-peach));
    border: 60px solid transparent;
    background-clip: padding-box, border-box;
  }
  .rosette {
    position: absolute; width: 110px; height: 110px; border-radius: 50%;
    background: radial-gradient(circle, var(--rosette-core) 0%, var(--rosette-light) 45%, var(--band-peach) 75%, rgba(241,201,154,0) 100%);
  }
  .rosette.top-left { left: 8px; top: 6px; }
  .rosette.top-right { right: 8px; top: 6px; }
  .rosette.bottom-left { left: 8px; bottom: 6px; }
  .rosette.bottom-right { right: 8px; bottom: 6px; }

  .panel {
    position: absolute; left: 97px; top: 95px; width: 1008px; height: 657px;
    border-radius: 42px; background: var(--panel);
    border: 2px solid var(--panel-edge);
  }

  .title { position: absolute; left: 0; top: 0; }
  .title text {
    font-family: "UnifrakturMaguntia", serif; font-size: 70px;
    fill: var(--title-grey);
  }
  .title .shade { fill: #3d3d3d; opacity: 0.35; }

  .gold-text {
    position: absolute; left: 0; width: 1200px; text-align: center;
    font-family: "Cormorant Garamond", serif; font-weight: 600;
    color: var(--gold); text-transform: uppercase; white-space: nowrap;
  }
  .lead { top: 296px; font-size: 29px; letter-spacing: 6px; }
  .sublead { top: 334px; font-size: 21px; letter-spacing: 4.4px; }
  .awarded {
    position: absolute; left: 285px; top: 478px;
    font-family: "Cormorant Garamond", serif; font-weight: 600;
    font-size: 21px; letter-spacing: 4.4px; color: var(--gold);
  }
  .company {
    position: absolute; left: 142px; top: 686px;
    font-family: "Cormorant Garamond", serif; font-weight: 500;
    font-size: 45px; color: var(--gold);
  }
  .sign-line { position: absolute; height: 2px; background: var(--gold-line); }
  .recipient-line { left: 346px; top: 445px; width: 516px; }
  .signature-line { left: 722px; top: 708px; width: 333px; }

  .watermark-icon { position: absolute; border-radius: 14px; opacity: 0.8; }
  .satellite { left: 983px; top: 121px; width: 114px; height: 79px; background: linear-gradient(135deg, var(--icon-light), var(--icon-mid)); }
  .film { left: 919px; top: 463px; width: 136px; height: 135px; background: radial-gradient(circle at 60% 60%, var(--icon-mid), var(--icon-light) 70%); }
  .dish { left: 135px; top: 577px; width: 72px; height: 86px; background: linear-gradient(160deg, var(--icon-light), var(--icon-mid)); }
  .tv { left: 477px; top: 549px; width: 122px; height: 135px; background: linear-gradient(180deg, var(--icon-light), var(--icon-mid)); }
</style>
</head>
<body>
<main class="certificate">
  <div class="border-band" role="img" aria-label="Guilloche border in peach and lilac"></div>
  <div class="rosette top-left" role="img" aria-label="Corner rosette ornament"></div>
  <div class="rosette top-right" role="img" aria-label="Corner rosette ornament"></div>
  <div class="rosette bottom-left" role="img" aria-label="Corner rosette ornament"></div>
  <div class="rosette bottom-right" role="img" aria-label="Corner rosette ornament"></div>

  <div class="panel"></div>

  <div class="watermark-icon satellite" role="img" aria-label="Faint satellite illustration"></div>
  <div class="watermark-icon film" role="img" aria-label="Faint film clapperboard and reel illustration"></div>
  <div class="watermark-icon dish" role="img" aria-label="Faint satellite dish illustration"></div>
  <div class="watermark-icon tv" role="img" aria-label="Faint internet television illustration"></div>

  <svg class="title" width="1200" height="320" viewBox="0 0 1200 320">
    <defs>
      <path id="title-arc" d="M 205 290 Q 600 105 1000 290"/>
      <path id="title-arc-shade" d="M 208 294 Q 603 109 1003 294"/>
    </defs>
    <text class="shade" text-anchor="middle"><textPath href="#title-arc-shade" startOffset="50%">Certificate of Achievement</textPath></text>
    <text text-anchor="middle"><textPath href="#title-arc" startOffset="50%">Certificate of Achievement</textPath></text>
  </svg>

  <p class="gold-text lead">This certificate is proudly</p>
  <p class="gold-text sublead">Presented for honorable achievement to</p>
  <div class="sign-line recipient-line"></div>
  <p class="awarded">AWARDED THIS DAY of</p>
  <p class="company">XYZ Company</p>
  <div class="sign-line signature-line"></div>
</main>
</body>
</html>
```